We are looking for a new website design for our SEO WEB Development Company. The URL is www.brightlanterndigital.example

We want it to be a more powerful representation of what we do. We are also looking for a number of designers that we will give continuous business to every month. The persons design we choose will also get a proposal to complete 4 - 6 new designs for us every month for our clients.

Be creative as you can in your design submissions. We really want to stand out!

Just to give you an idea of what we like look at this site: http://www.corvexsiteworks.example/

```html
<!DOCTYPE html>
<html lang="en">
<head>
<meta charset="utf-8">
<title>Lantern Interactive Group</title>
<link href="https://fonts.googleapis.com/css2?family=Arimo:wght@400;700&family=Tinos:ital@0;1&display=swap" rel="stylesheet">
<style>
:root{
  --page:#6b6b6d;
  --page-dark:#5a5a5c;
  --nav-dark:#111;
  --nav-pink:#e07ab0;
  --nav-arrow:#d0308e;
  --orange:#f7a21b;
  --silver-hi:#f4f4f6;
  --silver-lo:#a9a9b0;
  --panel-top:#ffffff;
  --panel-bottom:#8f86c6;
  --ink:#111;
  --magenta:#c0168a;
  --green:#2f7d1a;
  --blue:#1572b8;
  --black:#0d0d0d;
  --amber:#f29418;
  --follow:#2a5fd8;
}
*{margin:0;padding:0;box-sizing:border-box}
html,body{width:1200px;height:898px;overflow:hidden}
body{background:radial-gradient(circle at 40% 30%,var(--page) 0%,var(--page-dark) 100%);position:relative;font-family:"Arimo",Arial,sans-serif}
.nav a{position:absolute;top:61px;height:42px;border-radius:6px;background:linear-gradient(90deg,var(--nav-dark) 55%,var(--nav-pink) 100%);border:1px solid #333;color:#fff;font-weight:700;font-size:16px;text-decoration:none;display:flex;align-items:center;padding-left:30px;box-shadow:0 2px 3px rgba(0,0,0,.5)}
.nav a::before{content:"";position:absolute;left:10px;top:12px;border-left:10px solid var(--nav-arrow);border-top:9px solid transparent;border-bottom:9px solid transparent}
.nav a.home{font-size:26px;font-weight:400}
.nav a.home::before{border-left-color:#2fb84a}
.brand{position:absolute;left:6px;top:127px;width:330px;height:194px;border:5px solid #c8c8c8;outline:2px solid #555;background:linear-gradient(180deg,var(--panel-top),var(--panel-bottom))}
.brand p{position:absolute;left:32px;color:var(--orange);font-weight:700;font-size:33px}
.brand .l1{top:30px}.brand .l2{top:94px}
.hero{position:absolute;left:340px;top:127px;width:858px;height:194px;background:linear-gradient(180deg,#ddd,#aaa)}
.hero .art{position:absolute;left:3px;top:16px;right:3px;bottom:18px;background:linear-gradient(90deg,#f6f8fb 0%,#cfe4f5 35%,#3e8fd2 70%,#1d4f95 100%)}
.hero .tag{position:absolute;right:10px;top:60px;color:#fff;text-align:right;font-size:19px;letter-spacing:1px;line-height:1.2}
.hero .tag small{display:block;font-size:15px}
.pill{position:absolute;border-radius:50%;background:radial-gradient(ellipse at 50% 30%,var(--silver-hi),var(--silver-lo));box-shadow:0 2px 4px rgba(0,0,0,.5)}
.pill span{position:absolute;inset:9px 12px;border-radius:50%;display:flex;align-items:center;justify-content:center;text-align:center;color:#fff;font-weight:700;font-size:19px;line-height:1.1;box-shadow:inset 0 -10px 16px rgba(255,255,255,.35)}
.r1{top:328px;height:89px;width:190px}
.r2{top:428px;height:76px;width:186px}
.r2 span{inset:8px 12px;font-size:18px}
.magenta{background:var(--magenta)}.green{background:var(--green)}.blue{background:var(--blue)}.black{background:var(--black)}.amber{background:var(--amber)}
.intro{position:absolute;left:35px;top:530px;width:820px;font-family:"Tinos","Times New Roman",serif;font-style:italic;color:var(--ink)}
.intro .lead{font-size:23.5px;line-height:34px}
.intro .body{margin-top:20px;font-size:19px;line-height:28px}
.hl{color:var(--orange)}
.quote{position:absolute;left:888px;top:513px;width:312px;height:385px;border:5px solid #c8c8c8;border-right:none;border-bottom:none;background:linear-gradient(180deg,var(--panel-top),var(--panel-bottom))}
.quote p{margin:20px 0 0 30px;font-family:"Tinos","Times New Roman",serif;font-style:italic;font-size:22px;line-height:34px;color:var(--ink);white-space:nowrap}
.quote .btn{position:absolute;left:44px;top:132px;width:206px;height:90px;border-radius:50%;background:radial-gradient(ellipse at 50% 30%,var(--silver-hi),var(--silver-lo))}
.quote .btn span{position:absolute;inset:9px 14px;border-radius:50%;background:var(--blue);color:#111;font-size:15px;text-align:center;padding-top:6px;line-height:28px}
.follow{position:absolute;left:1058px;top:778px;color:var(--follow);font-size:21px;font-style:italic}
.social{position:absolute;left:1057px;top:817px;display:grid;grid-template-columns:repeat(3,26px);gap:16px 17px}
.social i{width:26px;height:26px;border-radius:3px;display:block}
</style>
</head>
<body>
<nav class="nav">
  <a class="home" style="left:9px;width:170px" href="#">Home</a>
  <a style="left:204px;width:169px" href="#">Creative Design</a>
  <a style="left:400px;width:170px" href="#">Website Design</a>
  <a style="left:597px;width:171px" href="#">Internet Marketing</a>
  <a style="left:793px;width:170px" href="#">IT Consulting</a>
  <a style="left:991px;width:172px" href="#">Contact Us</a>
</nav>

<div class="brand"><p class="l1">Lantern</p><p class="l2">Interactie Group</p></div>

<div class="hero">
  <div class="art" role="img" aria-label="Banner photo: close-up eye and magnifying glass on a blue gradient"></div>
  <div class="tag">Focusing on your brand<small>With the right Internet Marketing tools</small></div>
</div>

<div class="pill r1" style="left:0"><span class="magenta">Creative<br>Advertising</span></div>
<div class="pill r1" style="left:192px"><span class="green">Corporate<br>Identy</span></div>
<div class="pill r1" style="left:385px"><span class="blue">Print<br>Design</span></div>
<div class="pill r1" style="left:585px"><span class="black">Packaing</span></div>
<div class="pill r1" style="left:784px"><span class="amber">Web<br>Design</span></div>
<div class="pill r1" style="left:995px"><span class="blue">E Commerce</span></div>

<div class="pill r2" style="left:12px"><span class="blue" style="font-size:15px">WebApplication<br>Development</span></div>
<div class="pill r2" style="left:217px"><span class="amber">Multimedia</span></div>
<div class="pill r2" style="left:422px"><span class="black">SEO</span></div>
<div class="pill r2" style="left:621px"><span class="blue">SEM<br>Pay per click</span></div>
<div class="pill r2" style="left:815px"><span class="green">E mail<br>Marketing</span></div>
<div class="pill r2" style="left:1006px"><span class="magenta" style="font-size:13px">Reputation<br>Repair<br>Management</span></div>

<section class="intro">
  <p class="lead"><span class="hl">Lantern Interactive Group</span> is a leading Dallas Web Site Design,<br>Publishing and Internet Marketing Firm.<br>Our Dallas Texas based Website Design and Internet Marketing experts<br>&nbsp;are some of the best in the industry!</p>
  <p class="body"><span class="hl">Lantern Interactive Web</span> is a full-service Dallas based Advertising Agency<br>&nbsp;comprised of experienced advertising and marketing professionals that provide<br>clients with a clear and distinct voice in the marketplace. Web Site Design<br>and Internet Marketing experts at our Dallas location specialize in developing<br>Online Marketing Strategies, Search Engine Marketing and Optimization (SEO),<br>Pay Per Click , Web Site Design and Development, and Online Reputation Management.</p>
</section>

<aside class="quote">
  <p>Click on the link below to<br>begin filling out our<br>Request-A-Quote form</p>
  <div class="btn"><span>Request a<br>Quote</span></div>
</aside>
<div class="follow">Follow Us on</div>
<div class="social" aria-label="Social links">
  <i style="background:#2c3f8f"></i><i style="background:#3b5998"></i><i style="background:#2a6fa3"></i>
  <i style="background:#3d8c3a"></i><i style="background:#e8801d"></i><i style="background:#d9d9e6"></i>
</div>
</body>
</html>
```